Kestrel Valley Alpine Riders Society needs a business card design

We need a business card design for our newly incorporated KVARS. We are helping the NZ Chinese community, as well as everyone else, to organise ski & snowboarding trips, training, and equipments. The design should be creative, energetic, young and vibrant.

Industry/Entity Type

Social Club

Contact Information for Business Card

Logo; Kestrel Valley Alpine Riders Society; Name: Oliver Brandt; Position: President; Address: 42 Marwick Rd, Epsom, Auckland 1051; Mobile: 020 7826 1957; Email: oliver@kvars-club.example; Web: www.kvars-club.example

Requirements
Must have
• 1, The text "Kestrel Valley Alpine Riders Society" should be put together with the supplied logo file to form a new complete logo combination.
• 2, Final design files should be in Adobe Illustrator format and all text must be editable.
Nice to have
• two or three colours

```html
<!DOCTYPE html>
<html lang="en">
<head>
<meta charset="utf-8">
<title>Kestrel Valley Alpine Riders Society – Business Card</title>
<link rel="stylesheet" href="https://fonts.googleapis.com/css2?family=Source+Sans+3:wght@400;600;700;800&display=swap">
<style>
  :root {
    --navy: #263271;
    --sky: #2d9cd6;
    --stripe: #2595d3;
    --fold: #1b5ea3;
    --white: #ffffff;
    --font: "Source Sans 3", "Myriad Pro", Arial, sans-serif;
  }
  html, body {
    margin: 0;
    padding: 0;
    overflow: hidden;
    background: var(--white);
  }
  .card {
    position: relative;
    width: 1200px;
    height: 686px;
    overflow: hidden;
    background: var(--white);
    font-family: var(--font);
  }
  .card__backdrop {
    position: absolute;
    inset: 0;
  }
  .brand {
    position: absolute;
    left: 0;
    width: 1200px;
    top: 56px;
    margin: 0;
    text-align: center;
    color: var(--navy);
    font-weight: 800;
  }
  .brand__short {
    display: block;
    font-size: 160px;
    line-height: 1;
    letter-spacing: 2px;
  }
  .brand__full {
    display: block;
    margin-top: 14px;
    font-size: 34px;
    line-height: 1;
    letter-spacing: 1px;
  }
  .holder {
    position: absolute;
    left: 426px;
    top: 340px;
    color: var(--white);
  }
  .holder__name {
    margin: 0;
    padding-top: 6px;
    font-size: 54px;
    font-weight: 700;
    line-height: 1;
  }
  .holder__role {
    margin: 0;
    font-size: 42px;
    font-weight: 400;
    line-height: 1;
  }
  .contacts {
    position: absolute;
    top: 513px;
    left: 58px;
    display: grid;
    grid-template-columns: 462px auto;
    row-gap: 17px;
    margin: 0;
    padding: 0;
    list-style: none;
  }
  .contact {
    display: flex;
    align-items: center;
    gap: 24px;
    color: var(--white);
    font-size: 33px;
    line-height: 38px;
    white-space: nowrap;
  }
  .contact__icon {
    width: 30px;
    height: 30px;
    flex: none;
  }
</style>
</head>
<body>
<main class="card">
  <svg class="card__backdrop" width="1200" height="686" viewBox="0 0 1200 686" aria-hidden="true">
    <rect class="band-stripe" x="0" y="378" width="1200" height="11" fill="var(--stripe)"/>
    <rect class="band-main" x="0" y="399" width="1200" height="287" fill="var(--sky)"/>
    <polygon class="ribbon-fold" points="277,376 294,340 312,376" fill="var(--fold)"/>
    <polygon class="ribbon-fold" points="911,376 894,340 876,376" fill="var(--fold)"/>
    <polygon class="ribbon-outline" points="290,336 898,336 876,456 324,456" fill="var(--white)"/>
    <polygon class="ribbon" points="294,340 894,340 872,450 328,450" fill="var(--navy)"/>
  </svg>

  <h1 class="brand">
    <span class="brand__short">KVARS</span>
    <span class="brand__full">Kestrel Valley Alpine Riders Society</span>
  </h1>

  <section class="holder">
    <p class="holder__name">Oliver Brandt</p>
    <p class="holder__role">President</p>
  </section>

  <ul class="contacts">
    <li class="contact contact--phone">
      <svg class="contact__icon" viewBox="0 0 30 30" aria-hidden="true">
        <circle cx="15" cy="15" r="15" fill="var(--navy)"/>
        <path d="M10 8.5c1-.8 2-.6 2.5.3l1.2 2.3c.4.8.1 1.5-.6 2l-.7.5c.6 1.6 1.8 2.9 3.3 3.6l.6-.7c.5-.7 1.3-.9 2-.5l2.2 1.3c.9.5 1 1.6.2 2.4-1.2 1.3-2.6 1.6-4.2 1-3.5-1.4-6.1-4.1-7.2-7.6-.4-1.7.1-3.5.9-4.6z" fill="var(--white)"/>
      </svg>
      <span>020 7826 1957</span>
    </li>
    <li class="contact contact--web">
      <svg class="contact__icon" viewBox="0 0 30 30" aria-hidden="true">
        <circle cx="15" cy="15" r="15" fill="var(--navy)"/>
        <circle cx="17" cy="12.5" r="4.8" fill="none" stroke="var(--white)" stroke-width="2.4"/>
        <line x1="13.6" y1="16" x2="8.5" y2="21.2" stroke="var(--white)" stroke-width="3" stroke-linecap="round"/>
      </svg>
      <span>www.kvars-club.example</span>
    </li>
    <li class="contact contact--email">
      <svg class="contact__icon" viewBox="0 0 30 30" aria-hidden="true">
        <circle cx="15" cy="15" r="15" fill="var(--navy)"/>
        <rect x="8" y="10" width="14" height="10.5" rx="1.2" fill="var(--white)"/>
        <path d="M8.6 10.8l6.4 5 6.4-5" fill="none" stroke="var(--navy)" stroke-width="1.5"/>
      </svg>
      <span>oliver@kvars-club.example</span>
    </li>
    <li class="contact contact--address">
      <svg class="contact__icon" viewBox="0 0 30 30" aria-hidden="true">
        <circle cx="15" cy="15" r="15" fill="var(--navy)"/>
        <path d="M15 6.5c-3.4 0-6 2.6-6 5.9 0 4.2 6 10.6 6 10.6s6-6.4 6-10.6c0-3.3-2.6-5.9-6-5.9z" fill="var(--white)"/>
        <circle cx="15" cy="12.4" r="2.2" fill="var(--navy)"/>
      </svg>
      <span>42 Marwick Rd, Epsom, Auckland 1051</span>
    </li>
  </ul>
</main>
</body>
</html>
```